Business Card Design

Hello,
I try and keep my business card fresh and current. So about every year i get a new one. This year I'd like something with a white background and black lettering.
Before you start - I do not want my phone number or any other description on the card other than my url and my email.

I'd like a double sided business card with
TobFarnsby.com on one side

and

Tob@TobFarnsby.com on the other side of the card

Thinking very minimalistic and modern.
I don't have a particular font i mind or how to capitalize my name or website. This card will lead people to my new website that is being designed to showcase my photography and music.

* Initial thought was the front side of the card having a grid-like pattern built out of dashes or periods, with my website sitting within the pattern and on the back side my email on a stark white background. But that might look completely lame - haha.

I'm looking forward to seeing what you come up with.

thank you,
- tob farnsby

Reason: Want to spend some more time with the designs and add a little $. thanks for all the designs - tob

Wanted to add a little $ and spend some more time with the designs.

big thanks to all who have submitted work 

- tob

Industry/Entity Type

Business

Contact Information for Business Card

www.tobfarnsby.com
tob@tobfarnsby.com

Colors
000000
ffffff

Requirements
Must have
• tobfarnsby.com
tob@tobfarnsby.com
Should not have
• phone number
any description of what i do, photography or music

```html
<!DOCTYPE html>
<html lang="en">
<head>
<meta charset="utf-8">
<title>Tob Farnsby — Business Card</title>
<link rel="stylesheet" href="https://fonts.googleapis.com/css2?family=Comfortaa:wght@300;400&display=swap">
<style>
  :root {
    --backdrop: #ececec;
    --card: #ffffff;
    --ink: #000000;
    --card-shadow: rgba(0, 0, 0, 0.08);
  }
  html, body {
    margin: 0;
    padding: 0;
    width: 1200px;
    height: 720px;
    overflow: hidden;
    background: var(--backdrop);
  }
  .canvas {
    position: relative;
    width: 1200px;
    height: 720px;
    display: flex;
    align-items: center;
    justify-content: center;
    gap: 60px;
  }
  .card {
    position: relative;
    width: 525px;
    height: 300px;
    background: var(--card);
    box-shadow: 0 2px 10px var(--card-shadow);
    font-family: "Comfortaa", sans-serif;
    color: var(--ink);
    box-sizing: border-box;
  }
  .card-name {
    position: absolute;
    left: 40px;
    top: 74px;
    margin: 0;
    font-weight: 300;
    font-size: 58px;
    letter-spacing: 2px;
    line-height: 1;
    white-space: nowrap;
  }
  .card-url {
    position: absolute;
    left: 120px;
    bottom: 60px;
    margin: 0;
    font-weight: 300;
    font-size: 19px;
    letter-spacing: 2px;
    white-space: nowrap;
  }
  .card-email {
    position: absolute;
    right: 36px;
    bottom: 34px;
    margin: 0;
    font-weight: 300;
    font-size: 19px;
    letter-spacing: 2px;
    white-space: nowrap;
  }
</style>
</head>
<body>
  <main class="canvas">
    <section class="card card-front" aria-label="Card front">
      <h1 class="card-name">Tob Farnsby</h1>
      <p class="card-url">www.tobfarnsby.com</p>
    </section>
    <section class="card card-back" aria-label="Card back">
      <p class="card-email">tob@tobfarnsby.com</p>
    </section>
  </main>
</body>
</html>
```